Tasman Curdworks Guild needs new business cards

We need new business cards designed and produced. We are likely to need other design work done for ads, flyers etc in future.

We would like to start with an initial business card.

The Tasman Curdworks Guild (TCG) is a membership-based not-for-profit organisation that looks after the interests of Australia's small to medium artisan cheesemakers, many of whom are also small-scale farmers. The design should be simple, using our logo, but also communicate our artisan cheese and small dairy farm focus.

The first card to be designed and produced is for me, Miriam Tolhurst. My details are:

Miriam Tolhurst
Secretary
Tasman Curdworks Guild (TCG)
http://www.curdworksguild.example
T +61452837190
E miriam.miriamtolhurst@mailbox.example

I have attached the TCG logo in jpg form. I have a higher resolution version available if needed.

Thank you!

Miriam

Miriam Tolhurst
Tasman Curdworks Guild
miriam.miriamtolhurst@mailbox.example
+61452837190

Sans Serif

• Logo (see attached file)

```html
<!DOCTYPE html>
<html lang="en">
<head>
<meta charset="utf-8">
<title>Tasman Curdworks Guild – Business Card</title>
<link rel="stylesheet" href="https://fonts.googleapis.com/css2?family=EB+Garamond:wght@400;500&display=swap">
<style>
  :root {
    --backdrop: #2b2b2c;
    --card: #fbfbfa;
    --band: #4a2410;
    --band-text: #efe6dc;
    --brand-brown: #5a2e14;
    --name-brown: #7a4522;
    --ink: #1f1f1f;
    --cheese-gold: #e9b53f;
  }
  * { box-sizing: border-box; margin: 0; padding: 0; }
  html, body {
    width: 1200px;
    height: 997px;
    overflow: hidden;
    background: var(--backdrop);
  }
  body {
    display: flex;
    align-items: center;
    justify-content: center;
    font-family: "EB Garamond", Georgia, serif;
  }
  .business-card {
    position: relative;
    width: 900px;
    height: 514px;
    background: var(--card);
    box-shadow: 0 18px 40px rgba(0,0,0,0.45);
    overflow: hidden;
  }
  .brand {
    position: absolute;
    left: 80px;
    top: 170px;
    display: flex;
    align-items: center;
    gap: 22px;
  }
  .brand-dot {
    width: 92px;
    height: 92px;
    border-radius: 50%;
    background: var(--cheese-gold);
    flex: none;
  }
  .brand-name {
    font-size: 38px;
    line-height: 1.0;
    font-weight: 400;
    color: var(--brand-brown);
    width: 230px;
  }
  .divider {
    position: absolute;
    left: 445px;
    top: 120px;
    width: 2px;
    height: 210px;
    background: linear-gradient(to bottom, rgba(90,46,20,0.1), var(--brand-brown) 45%, rgba(90,46,20,0.1));
  }
  .contact {
    position: absolute;
    left: 490px;
    top: 130px;
  }
  .contact-name {
    font-size: 27px;
    color: var(--name-brown);
    font-weight: 400;
  }
  .contact-role {
    font-size: 17px;
    color: var(--ink);
    margin: 6px 0 26px;
  }
  .contact-line {
    display: flex;
    align-items: center;
    gap: 14px;
    font-size: 18px;
    color: var(--ink);
    margin-bottom: 16px;
  }
  .contact-icon {
    width: 26px;
    height: 26px;
    flex: none;
  }
  .footer-band {
    position: absolute;
    left: 0;
    bottom: 0;
    width: 100%;
    height: 58px;
    background: var(--band);
    display: flex;
    align-items: center;
    padding-left: 250px;
    font-size: 21px;
    letter-spacing: 0.3px;
    color: var(--band-text);
  }
</style>
</head>
<body>
  <article class="business-card">
    <div class="brand">
      <span class="brand-dot"></span>
      <span class="brand-name">Tasman Curdworks Guild</span>
    </div>

    <div class="divider"></div>

    <section class="contact">
      <h1 class="contact-name">Miriam Tolhurst</h1>
      <p class="contact-role">Secretary</p>
      <p class="contact-line">
        <svg class="contact-icon" viewBox="0 0 26 26" aria-hidden="true">
          <circle cx="13" cy="13" r="13" fill="var(--band)"/>
          <path d="M7 10c0-1.5 3-3 6-3s6 1.5 6 3l-2.5 1-1-2h-5l-1 2z M8 19l2-6h6l2 6z" fill="#fff"/>
          <circle cx="13" cy="16" r="1.6" fill="var(--band)"/>
        </svg>
        <span>+61452837190</span>
      </p>
      <p class="contact-line">
        <svg class="contact-icon" viewBox="0 0 26 26" aria-hidden="true">
          <circle cx="13" cy="13" r="13" fill="var(--band)"/>
          <rect x="6.5" y="8.5" width="13" height="9" fill="#fff"/>
          <path d="M6.5 8.5l6.5 5.5 6.5-5.5" fill="none" stroke="var(--band)" stroke-width="1.2"/>
        </svg>
        <span>miriam.miriamtolhurst@mailbox.example</span>
      </p>
    </section>

    <footer class="footer-band">Tasman Curdworks Guild (TCG)</footer>
  </article>
</body>
</html>
```